Custom Framing Shop Stonebrook Framing Studio

I want an eye catching graphic that will be used a s business sign on a busy road. The sign MUST communicate the type of business it is clearly to vehicles traveling at 40 mph. This is a custom picture framing business and the sign will be hanging and be approximately 32" X 48". The business name is Stonebrook Framing Studio; Custom framing: by appointment and should include a whole or partial image of a picture frame as a visual que. I've included inspiration idea's, color pallets and styles that I like and a current business card for inspiration. I like the crimson font style shadowing and background colors of the attached Pello's pizzeria sign. I'd prefer crimson letters. Custom Framing is the message to communicate, followed by phone number and business name. I like the idea of a shield shape with a banner since it would more eye catching, Once again the Stonebrook image and name is less important than communicating what the business does. I like Crimson, grey, gold, black but am open to new ideas . I like the idea of a shield with a banner more than a rectangle, but am open to idea's

Target Market(s)

My target market is local homeowners ($700k+) who want a relationship with their framer and are willing to pay for a customized experience compared to a craft store experience. I have more female clients then men.

Industry/Entity Type

Picture Framing Art

Other font styles liked:
• Look at the attached image of a custom pizzeria sign, its kid of a custom car pinstripe font style. Script and decorative may be difficult to read while driving by but add to the elegance.

Colors

Designer to choose colors to be used in the design.

Requirements
Must have
• Clearly communicate what the business does "Custom framing" preferably with a picture frame and words
Nice to have
• incorporate a Stonebrook into the graphic
Should not have
• A Stonebrook image doesn't communicate what the business does to a vehicle traveling at 40 mph by the sign

```html
<!DOCTYPE html>
<html lang="en">
<head>
<meta charset="utf-8">
<title>Stonebrook Framing Studio – Custom Framing Sign</title>
<link href="https://fonts.googleapis.com/css2?family=Alfa+Slab+One&display=swap" rel="stylesheet">
<style>
  :root {
    --crimson: #851c19;
    --gold: #c98f38;
    --gold-light: #d7a555;
    --charcoal: #2e2e2c;
    --cream: #f0d7b0;
    --paper: #ffffff;
  }
  html, body {
    margin: 0;
    padding: 0;
    width: 800px;
    height: 1200px;
    overflow: hidden;
    background: var(--paper);
  }
  .sign {
    display: block;
    width: 800px;
    height: 1200px;
  }
  .sign-text {
    font-family: "Alfa Slab One", Georgia, serif;
  }
  .band-crimson { fill: none; stroke: var(--crimson); stroke-width: 190; stroke-linejoin: round; }
  .band-gold { fill: none; stroke: var(--gold); stroke-width: 150; stroke-linejoin: round; }
  .band-charcoal { fill: none; stroke: var(--charcoal); stroke-width: 100; stroke-linejoin: round; }
  .field { fill: var(--cream); }
  .inner-rule { fill: none; stroke: var(--gold-light); stroke-width: 9; vector-effect: non-scaling-stroke; }
  .brand-name { fill: var(--charcoal); font-size: 78px; letter-spacing: 4px; }
  .brand-mark { fill: none; stroke: var(--crimson); stroke-width: 9; }
  .headline-shadow { fill: var(--gold); }
  .headline {
    fill: var(--charcoal);
    stroke: var(--cream);
    stroke-width: 16;
    paint-order: stroke fill;
    stroke-linejoin: round;
  }
  .divider { fill: var(--charcoal); }
  .frames-art { fill: url(#framesTone); }
</style>
</head>
<body>
<svg class="sign" viewBox="0 0 1531 2300" preserveAspectRatio="none" xmlns="http://www.w3.org/2000/svg">
  <defs>
    <path id="shieldOutline" d="M765 92 Q470 100 270 235 L175 245 L175 350 L110 365 L100 440 L100 1540 Q150 1560 170 1600 L170 1880 Q400 2180 765 2205 Q1130 2180 1360 1880 L1360 1600 Q1380 1560 1431 1540 L1431 440 L1421 365 L1356 350 L1356 245 L1262 235 Q1060 100 765 92 Z"/>
    <linearGradient id="framesTone" x1="0" y1="0" x2="1" y2="1">
      <stop offset="0" stop-color="#5a514a"/>
      <stop offset="0.5" stop-color="#3a3835"/>
      <stop offset="1" stop-color="#6b5a44"/>
    </linearGradient>
  </defs>

  <!-- Shield bands -->
  <g class="shield">
    <use href="#shieldOutline" class="band-crimson"/>
    <use href="#shieldOutline" class="band-gold"/>
    <use href="#shieldOutline" class="band-charcoal"/>
    <use href="#shieldOutline" class="field"/>
    <use href="#shieldOutline" class="inner-rule" transform="translate(765 1150) scale(0.967 0.978) translate(-765 -1150)"/>
  </g>

  <!-- Brand -->
  <g class="brand sign-text">
    <rect class="brand-mark" x="528" y="250" width="60" height="60"/>
    <text class="brand-name" x="610" y="316" textLength="400" lengthAdjust="spacingAndGlyphs">STONEBROOK</text>
  </g>

  <!-- Headline -->
  <g class="sign-text">
    <text class="headline-shadow" x="280" y="677" font-size="280" textLength="1017" lengthAdjust="spacingAndGlyphs">CUSTOM</text>
    <text class="headline" x="258" y="645" font-size="280" textLength="1007" lengthAdjust="spacingAndGlyphs">CUSTOM</text>

    <text class="headline-shadow" x="228" y="944" font-size="280" textLength="1108" lengthAdjust="spacingAndGlyphs">FRAMING</text>
    <text class="headline" x="212" y="912" font-size="280" textLength="1100" lengthAdjust="spacingAndGlyphs">FRAMING</text>
  </g>

  <!-- Divider -->
  <g class="divider">
    <path d="M232 1020 L745 1002 L752 1018 L745 1030 Z"/>
    <path d="M1300 1020 L787 1002 L780 1018 L787 1030 Z"/>
    <path d="M767 972 L785 1002 L767 1032 L749 1002 Z"/>
  </g>

  <!-- Phone -->
  <g class="sign-text">
    <text class="headline-shadow" x="222" y="1266" font-size="215" textLength="1118" lengthAdjust="spacingAndGlyphs">+987654321</text>
    <text class="headline" x="200" y="1240" font-size="215" textLength="1110" lengthAdjust="spacingAndGlyphs">+987654321</text>
  </g>

  <!-- Picture frame artwork area -->
  <rect class="frames-art" x="350" y="1345" width="850" height="745" rx="24" role="img" aria-label="Illustration of four overlapping picture frames in charcoal with gold and cream edges"/>
</svg>
</body>
</html>
```